RT Pemberly Electric Yard Sign

Looking to have a yard sign designed that we can place at projects we are working on. Most likely will be 18" H x 24" W but flexible that we can increase the size if necessary. It should include our logo, our phone # 609-555-0147, website rtpemberlyelectric-example.com and slogan, built on integrity, driven by excellence. Colors should match our brand.

```html
<!DOCTYPE html>
<html lang="en">
<head>
<meta charset="utf-8">
<title>RT Pemberly Electric Yard Sign</title>
<link href="https://fonts.googleapis.com/css2?family=Bebas+Neue&family=Jost:wght@500&display=swap" rel="stylesheet">
<style>
  :root {
    --backdrop: #505050;
    --sign-white: #ffffff;
    --brand-navy: #05355a;
    --brand-red: #e3202b;
    --text-light: #ffffff;
  }
  * { margin: 0; padding: 0; box-sizing: border-box; }
  html, body {
    width: 1200px; height: 1001px; overflow: hidden;
    background: var(--backdrop);
  }
  .yard-sign {
    position: absolute; left: 128px; top: 146px;
    width: 944px; height: 708px;
    display: flex; flex-direction: column;
  }
  .brand-panel {
    height: 301px; background: var(--sign-white);
    display: flex; flex-direction: column; align-items: center; justify-content: flex-end;
    padding-bottom: 34px;
  }
  .brand-name-row { display: flex; align-items: center; gap: 18px; }
  .brand-mark { width: 40px; height: 40px; background: var(--brand-red); }
  .brand-name {
    font-family: "Bebas Neue", sans-serif; font-size: 78px; line-height: 1;
    color: var(--brand-red); letter-spacing: 3px;
  }
  .brand-descriptor {
    font-family: "Jost", sans-serif; font-weight: 500; font-size: 33px;
    color: var(--brand-navy); letter-spacing: 5px; margin-top: 6px;
  }
  .brand-rule {
    width: 544px; height: 5px; margin-top: 8px;
    background: var(--brand-red); border-bottom: 2px solid var(--brand-navy);
  }
  .contact-panel {
    height: 287px; background: var(--brand-navy);
    padding: 24px 0 0 68px;
  }
  .contact-line { display: flex; align-items: center; color: var(--text-light); font-family: "Bebas Neue", sans-serif; }
  .contact-line svg { flex: none; }
  .contact-phone { font-size: 168px; line-height: 1; letter-spacing: 1px; }
  .contact-phone svg { margin-right: 22px; margin-top: -16px; }
  .contact-web { font-size: 64px; line-height: 1; margin-top: 2px; }
  .contact-web svg { margin-right: 22px; margin-top: -6px; }
  .slogan-panel {
    flex: 1; background: var(--brand-red);
    display: flex; align-items: center; justify-content: center;
  }
  .slogan {
    font-family: "Bebas Neue", sans-serif; font-size: 56px; color: var(--text-light);
    transform: skewX(-10deg); letter-spacing: 0.5px;
  }
</style>
</head>
<body>
  <main class="yard-sign">
    <section class="brand-panel">
      <div class="brand-name-row">
        <span class="brand-mark"></span>
        <span class="brand-name">RT Pemberly Electric</span>
      </div>
      <div class="brand-descriptor">Electrical Contractor</div>
      <div class="brand-rule"></div>
    </section>
    <section class="contact-panel">
      <div class="contact-line contact-phone">
        <svg width="38" height="52" viewBox="0 0 24 32" aria-hidden="true">
          <path fill="#e3202b" d="M6 1 L10 8 L7 11 C8 16 11 21 15 24 L18 21 L24 26 L20 31 C10 29 2 18 1 6 Z"/>
        </svg>
        <span>609-555-0147</span>
      </div>
      <div class="contact-line contact-web">
        <svg width="42" height="42" viewBox="0 0 40 40" aria-hidden="true">
          <g fill="none" stroke="#e3202b" stroke-width="3">
            <circle cx="20" cy="20" r="17"/>
            <ellipse cx="20" cy="20" rx="8" ry="17"/>
            <line x1="3" y1="20" x2="37" y2="20"/>
            <line x1="20" y1="3" x2="20" y2="37"/>
            <line x1="6" y1="11" x2="34" y2="11"/>
            <line x1="6" y1="29" x2="34" y2="29"/>
          </g>
        </svg>
        <span>RTPEMBERLYELECTRIC-EXAMPLE.COM</span>
      </div>
    </section>
    <section class="slogan-panel">
      <p class="slogan">Built on integrity, driven by excellence</p>
    </section>
  </main>
</body>
</html>
```